Ridgeline Outfitters Business Cards

Recently had a logo done with Artfolio and now looking for a business card to go along with it.

Target Market(s)

Ridgeline Outfitters is a weapons dealer. My market will be primarily men, hunting, shooting type.

Industry/Entity Type

Business

Contact Information for Business Card

I selected double sided, but this is not required, single or double is going to be fine. I picture the logo on one side, or perhaps just the circle which contains "RO" with the remaining info on the other side.

Font styles to use
Sans Serif

Requirements
Must have
• My name: Milo Brandt
• Title: Owner
• tel: 612-555-0187
• web: www.ridgelineoutfittersmn.example
Nice to have
• I like the concept of a black business card. I would like to keep the colors monotone, black, grey, white or red. Red is acceptable because it is in the logo. I have also seen cards that are matte black with shiny black as well, perhaps for the logo (or circle RO) part of the logo.
• I will upload a couple of the logos for use, and also an example I just found of the black on black. and some others that have a nice contrast.
Should not have
• lots of colors are not wanted.

```html
<!DOCTYPE html>
<html lang="en">
<head>
<meta charset="utf-8">
<title>Ridgeline Outfitters Business Cards</title>
<link rel="stylesheet" href="https://fonts.googleapis.com/css2?family=Josefin+Sans:wght@300;400;600&display=swap">
<style>
  :root {
    --bg: #2b2b2b;
    --card-black: #1f1f20;
    --emboss: #2c2c2d;
    --emboss-edge: #161617;
    --paper: #f2f2f2;
    --red: #e2232b;
    --grey: #8a8a8a;
    --white: #ffffff;
  }
  * { box-sizing: border-box; margin: 0; padding: 0; }
  html, body { width: 1200px; height: 834px; overflow: hidden; }
  body {
    background: radial-gradient(ellipse at center, #3a3a3a 0%, var(--bg) 70%);
    font-family: "Josefin Sans", sans-serif;
    position: relative;
  }
  .card {
    position: absolute;
    top: 267px;
    width: 525px;
    height: 300px;
    border-radius: 2px;
    overflow: hidden;
    box-shadow: 0 10px 30px rgba(0,0,0,.45);
  }
  .card--front { left: 50px; background: var(--card-black); }
  .card--back { left: 625px; background: var(--card-black); }

  .brand { display: flex; align-items: center; gap: 16px; }
  .brand__circle { border-radius: 50%; flex: none; }
  .brand__name {
    font-weight: 600;
    letter-spacing: 2px;
    text-transform: uppercase;
    white-space: nowrap;
  }

  .card--front .brand {
    position: absolute; left: 0; right: 0; top: 0; bottom: 0;
    justify-content: center;
  }
  .card--front .brand__circle {
    width: 84px; height: 84px;
    border: 3px solid var(--emboss);
    box-shadow: 0 1px 0 var(--emboss-edge);
  }
  .card--front .brand__name {
    color: var(--emboss);
    font-size: 27px;
    text-shadow: 0 1px 0 var(--emboss-edge), 0 -1px 0 #333335;
  }

  .card__band {
    height: 138px;
    background: var(--paper);
  }
  .card--back .brand {
    height: 100%;
    justify-content: center;
  }
  .card--back .brand__circle {
    width: 54px; height: 54px;
    border: 3px solid var(--grey);
  }
  .card--back .brand__name { color: var(--red); font-size: 21px; }

  .person {
    position: absolute; left: 40px; bottom: 44px;
  }
  .person__name {
    color: var(--white);
    font-size: 21px;
    font-weight: 300;
    text-transform: uppercase;
    letter-spacing: .5px;
  }
  .person__title { color: var(--red); font-size: 14px; margin-top: 3px; }

  .contact {
    position: absolute; left: 235px; top: 172px;
    list-style: none;
  }
  .contact__item {
    display: flex; align-items: center; gap: 10px;
    color: var(--white);
    font-size: 13px;
    font-weight: 300;
    margin-bottom: 12px;
  }
  .contact__icon { width: 14px; height: 14px; flex: none; }
</style>
</head>
<body>
  <section class="card card--front" aria-label="Card front">
    <div class="brand">
      <span class="brand__circle"></span>
      <span class="brand__name">Ridgeline Outfitters</span>
    </div>
  </section>

  <section class="card card--back" aria-label="Card back">
    <div class="card__band">
      <div class="brand">
        <span class="brand__circle"></span>
        <span class="brand__name">Ridgeline Outfitters</span>
      </div>
    </div>

    <div class="person">
      <p class="person__name">Milo Brandt</p>
      <p class="person__title">Owner</p>
    </div>

    <ul class="contact">
      <li class="contact__item">
        <svg class="contact__icon" viewBox="0 0 24 24" fill="none" stroke="#e2232b" stroke-width="2">
          <path d="M5 3h4l2 5-3 2a12 12 0 0 0 6 6l2-3 5 2v4a2 2 0 0 1-2 2A17 17 0 0 1 3 5a2 2 0 0 1 2-2z"/>
        </svg>
        <span>612-555-0187</span>
      </li>
      <li class="contact__item">
        <svg class="contact__icon" viewBox="0 0 24 24" fill="none" stroke="#e2232b" stroke-width="2">
          <circle cx="12" cy="12" r="9"/>
          <path d="M3 12h18M12 3c3 3 3 15 0 18M12 3c-3 3-3 15 0 18"/>
        </svg>
        <span>www.ridgelineoutfittersmn.example</span>
      </li>
    </ul>
  </section>
</body>
</html>
```